Non-profit wants to save the world needs Wordpress presence

My name is Tomas Verdugo. I'm a photographer who started a charity (Rancho las Brumas) to help the rural schools and health clinics in Central America. We distribute schools supplies and help health clinics with much needed medical supplies and equipment. I need a way to accept donations. I need to have several different writers post to the blog (in Spanish and English). I have a domain name registered (www.rancholasbrumas.org) and started a simple wordpress site as well at http://www.rancholasbrumas.blogsite.com

Industry/Entity Type

Charity

```html
<!DOCTYPE html>
<html lang="en">
<head>
<meta charset="utf-8">
<title>Rancho las Brumas</title>
<link rel="stylesheet" href="https://fonts.googleapis.com/css2?family=Source+Sans+3:wght@400;600;700&display=swap">
<style>
:root{
  --frame:#333333;
  --page:#f3f3f3;
  --blue:#2ea2d6;
  --blue-dark:#1778a8;
  --footer:#1f8ec3;
  --bottom:#454545;
  --ink:#3a3a3a;
  --muted:#6b6b6b;
  --link:#3d9bc4;
  --green:#8cc63f;
  --rule:#d6d6d6;
}
*{margin:0;padding:0;box-sizing:border-box}
html,body{width:750px;height:1200px;overflow:hidden}
body{background:var(--frame);font-family:"Source Sans 3",Arial,sans-serif;color:var(--ink);position:relative}
.abs{position:absolute}
.page{left:62px;top:0;width:624px;height:986px;background:var(--page)}
.brand{left:66px;top:16px;width:82px;display:flex;align-items:center;gap:5px}
.brand-dot{flex:none;width:14px;height:14px;border-radius:50%;background:#7ab648}
.brand-name{font-size:12px;font-weight:700;line-height:13px;color:#2f6b2a}
.tagline{left:157px;top:27px;font-size:15px;font-weight:600;color:#4a4a4a}
.donate-badge{left:452px;top:13px;width:73px;height:49px;background:linear-gradient(#8fc740,#6faa2b);border:1px solid #5f9a22;color:#fff;text-align:center;padding-top:9px}
.donate-badge strong{display:block;font-size:12px;font-weight:700;line-height:14px}
.donate-badge small{display:block;font-size:6px;line-height:10px;margin-top:5px}
.social{left:593px;top:19px;display:flex;gap:6px}
.social span{width:14px;height:14px;display:block}
.search{left:540px;top:40px;width:127px;height:20px;background:#fff;border:1px solid #c9c9c9;border-radius:2px;font-size:8px;font-style:italic;color:#777;padding:4px 7px}
.search svg{position:absolute;right:6px;top:3px}
.nav{left:56px;top:77px;width:636px;height:27px;background:var(--blue)}
.nav-tab{left:155px;top:73px;width:44px;height:30px;background:var(--blue-dark)}
.nav-item{top:84px;font-size:12px;font-weight:700;color:#fff}
.slider{left:62px;top:117px;width:624px;height:228px;background:linear-gradient(100deg,#6f7d4a 0%,#8a8a66 35%,#9c8f72 55%,#4e5e34 100%)}
.arrow{top:221px;width:28px;height:28px;border-radius:50%;background:rgba(225,225,225,.85)}
.dots{left:354px;top:330px;width:42px;height:11px;background:#eee;border-radius:2px;display:flex;gap:3px;align-items:center;justify-content:center}
.dots i{width:5px;height:5px;border-radius:50%;background:#555;display:block}
.dots i.on{background:var(--blue)}
.shadow{left:80px;top:358px;width:590px;height:16px;background:radial-gradient(ellipse at center,rgba(0,0,0,.28) 0%,rgba(0,0,0,0) 70%)}
.feature{left:80px;top:402px;width:242px;height:237px;background:#1c1c1c;padding:5px}
.feature-photo{width:232px;height:227px;background:linear-gradient(#7fb0d6,#b69a7a 60%,#5d4a3a)}
.feature-caption{left:5px;bottom:5px;width:232px;height:61px;background:rgba(0,0,0,.6);padding:6px 8px;color:#fff}
.feature-caption h3{font-size:11px;font-weight:600;margin-bottom:3px}
.feature-caption p{font-size:6px;line-height:8px}
.heading{font-size:15px;font-weight:600;color:#333;letter-spacing:.3px}
.fp-thumb{left:79px;top:705px;width:65px;height:65px;border:1px solid #ddd;background:linear-gradient(#e8ecef 55%,#b9783c)}
.fp-text{left:153px;top:704px;width:160px}
.fp-text h4{font-size:10.5px;font-weight:600;margin-bottom:2px}
.fp-text p{font-size:7.5px;line-height:10px;color:#555}
.fp-text a{font-size:7.5px;font-weight:700;color:#1f5fa8;text-decoration:none}
.video{left:82px;top:800px;width:203px;height:121px;background:linear-gradient(120deg,#4d5a3a,#6e7058 50%,#3f4a2e)}
.video-bar{left:0;bottom:0;width:100%;height:7px;background:#111}
.latest-rule{left:340px;top:421px;width:323px;height:5px;border:1px dashed #c7c7c7;border-radius:3px}
.post-thumb{left:343px;width:115px;height:79px;border:3px solid #fff;box-shadow:0 0 2px #bbb}
.post-body{left:473px;width:186px}
.post-body h4{font-size:10.5px;font-weight:400;line-height:13px;color:#333}
.post-meta{font-size:6px;color:var(--link);margin:4px 0 3px;position:relative}
.post-meta .share{position:absolute;right:16px;top:-4px;display:flex;gap:3px}
.post-meta .share span{width:10px;height:10px;border-radius:50%;background:#777;display:block}
.post-body p{font-size:5px;line-height:7.8px;color:#555}
.post-rule{left:340px;width:323px;height:2px;background:var(--rule)}
.footer{left:0;top:986px;width:750px;height:187px;background:var(--footer);color:#fff}
.f-head{top:1003px;font-size:18px;font-weight:600;color:#fff}
.f-list{top:1033px;font-size:12px;font-weight:600;line-height:18px;color:#e8f4fa;list-style:none}
.tags{left:382px;top:1029px;width:120px;font-size:12px;font-weight:600;line-height:19px;color:#e8f4fa}
.email{left:529px;top:1036px;width:130px;height:25px;background:#fff;border:2px solid #c9c9c9;border-radius:3px;font-size:8px;font-style:italic;color:#777;text-align:center;padding-top:6px}
.submit{left:551px;top:1078px;width:86px;height:24px;background:var(--green);color:#fff;font-size:11.5px;font-weight:600;text-align:center;padding-top:4px}
.bottom{left:0;top:1173px;width:750px;height:27px;background:var(--bottom);color:#ddd;font-size:8px;text-align:center;padding-top:9px}
</style>
</head>
<body>
<div class="abs page"></div>

<header>
  <div class="abs brand"><span class="brand-dot"></span><span class="brand-name">Rancho las<br>Brumas</span></div>
  <div class="abs tagline">Cultivando la paz y puro amor</div>
  <a class="abs donate-badge" href="#" aria-label="Donate now"><strong>Donate</strong><small>Click to Donate Now!</small></a>
  <div class="abs social" aria-label="Social links">
    <span style="background:#3b5998"></span><span style="background:#2fb3e8"></span><span style="background:#dd4b39"></span><span style="background:#f48a1e"></span>
  </div>
  <div class="abs search">Search post
    <svg width="12" height="12" viewBox="0 0 12 12"><circle cx="5" cy="5" r="3.6" fill="none" stroke="#2a6a9a" stroke-width="1.6"/><line x1="7.6" y1="7.6" x2="11" y2="11" stroke="#2a6a9a" stroke-width="1.8"/></svg>
  </div>
</header>

<nav>
  <div class="abs nav"></div>
  <div class="abs nav-tab"></div>
  <span class="abs nav-item" style="left:160px">Home</span>
  <span class="abs nav-item" style="left:210px">About Me</span>
  <span class="abs nav-item" style="left:278px">Our Projects</span>
  <span class="abs nav-item" style="left:361px">Blogs</span>
  <span class="abs nav-item" style="left:409px">News</span>
  <span class="abs nav-item" style="left:456px">Support Us</span>
  <span class="abs nav-item" style="left:534px">Contact Us</span>
</nav>

<section>
  <div class="abs slider" role="img" aria-label="Photo of children walking a rural village path while a photographer kneels to take pictures"></div>
  <div class="abs arrow" style="left:66px"><svg width="28" height="28"><path d="M16 8 L10 14 L16 20" fill="none" stroke="#444" stroke-width="3"/></svg></div>
  <div class="abs arrow" style="left:652px"><svg width="28" height="28"><path d="M12 8 L18 14 L12 20" fill="none" stroke="#444" stroke-width="3"/></svg></div>
  <div class="abs dots"><i></i><i class="on"></i><i></i><i></i></div>
  <div class="abs shadow"></div>
</section>

<main>
  <div class="abs feature">
    <div class="feature-photo" role="img" aria-label="Photo of smiling schoolchildren standing together"></div>
    <div class="abs feature-caption">
      <h3>Lorem Ipsum Dolorum</h3>
      <p>Lorem ipsum dolor sit amet, consectetur adipisicing elit, sed do eiusmod tempor incididunt ut labore et dolore magna aliqua. Ut enim ad minim veniam.</p>
    </div>
  </div>

  <h2 class="abs heading" style="left:80px;top:674px">FEATURED POST</h2>
  <div class="abs fp-thumb" role="img" aria-label="Photo of a desk with a laptop"></div>
  <div class="abs fp-text">
    <h4>Lorem ipsum dolor sit amet,</h4>
    <p>consectetur adipisicing elit, sed do eiusmod tempor incididunt ut labore et dolore magna aliqua. Ut enim ad minim veniam, quis nostrud exercitation ullamco laboris.</p>
    <a href="#">MORE &gt;&gt;</a>
  </div>

  <div class="abs video" role="img" aria-label="Video still of a photographer in a village">
    <svg class="abs" style="left:81px;top:39px" width="42" height="42"><circle cx="21" cy="21" r="19" fill="rgba(0,0,0,.35)" stroke="#fff" stroke-width="2.5"/><path d="M16 12 L30 21 L16 30 Z" fill="#fff"/></svg>
    <div class="abs video-bar"></div>
  </div>

  <h2 class="abs heading" style="left:341px;top:399px;font-size:13px">LATEST POSTS</h2>
  <div class="abs latest-rule"></div>

  <div class="abs post-thumb" style="top:436px;background:linear-gradient(90deg,#8a6a3c 40%,#2f8a5a)" role="img" aria-label="Photo of a man beside a market stall"></div>
  <div class="abs post-body" style="top:436px">
    <h4>Lorem ipsum dolor sit amet, consect etur adipisicing elit...</h4>
    <div class="post-meta">September 24 &nbsp;•&nbsp; 14 Comments<span class="share"><span></span><span></span><span></span></span></div>
    <p>Lorem ipsum dolor sit amet, consectetur adipisicing elit, sed do eiusmod tempor incididunt ut labore et dolore magna aliqua. Ut enim ad minim veniam, quis nostrud exercitation.</p>
  </div>
  <div class="abs post-rule" style="top:529px"></div>

  <div class="abs post-thumb" style="top:574px;background:linear-gradient(90deg,#9fb3a0,#c98a6a)" role="img" aria-label="Photo of two girls smiling"></div>
  <div class="abs post-body" style="top:574px">
    <h4>Lorem ipsum dolor sit amet, consect etur adipisicing elit...</h4>
    <div class="post-meta">September 24 &nbsp;•&nbsp; 14 Comments<span class="share"><span></span><span></span><span></span></span></div>
    <p>Lorem ipsum dolor sit amet, consectetur adipisicing elit, sed do eiusmod tempor incididunt ut labore et dolore magna aliqua. Ut enim ad minim veniam, quis nostrud exercitation.</p>
  </div>
  <div class="abs post-rule" style="top:667px"></div>

  <div class="abs post-thumb" style="top:712px;background:linear-gradient(#5a6e3a,#8a7a5e)" role="img" aria-label="Photo of children on a village path"></div>
  <div class="abs post-body" style="top:712px">
    <h4>Lorem ipsum dolor sit amet, consect etur adipisicing elit...</h4>
    <div class="post-meta">September 24 &nbsp;•&nbsp; 14 Comments<span class="share"><span></span><span></span><span></span></span></div>
    <p>Lorem ipsum dolor sit amet, consectetur adipisicing elit, sed do eiusmod tempor incididunt ut labore et dolore magna aliqua. Ut enim ad minim veniam, quis nostrud exercitation.</p>
  </div>
  <div class="abs post-rule" style="top:805px"></div>

  <div class="abs post-thumb" style="top:850px;background:linear-gradient(90deg,#2f8a5a,#8a6a3c 60%)" role="img" aria-label="Photo of a man beside a market stall"></div>
  <div class="abs post-body" style="top:850px">
    <h4>Lorem ipsum dolor sit amet, consect etur adipisicing elit...</h4>
    <div class="post-meta">September 24 &nbsp;•&nbsp; 14 Comments<span class="share"><span></span><span></span><span></span></span></div>
    <p>Lorem ipsum dolor sit amet, consectetur adipisicing elit, sed do eiusmod tempor incididunt ut labore et dolore magna aliqua. Ut enim ad minim veniam, quis nostrud exercitation.</p>
  </div>
  <div class="abs post-rule" style="top:943px"></div>
</main>

<footer>
  <div class="abs footer"></div>
  <h3 class="abs f-head" style="left:98px">Quick Links</h3>
  <ul class="abs f-list" style="left:117px">
    <li>Home</li><li>About Us</li><li>Our Projects</li><li>Blogs</li><li>News</li><li>Support Us</li><li>Contact Us</li>
  </ul>
  <h3 class="abs f-head" style="left:256px">Archives</h3>
  <ul class="abs f-list" style="left:259px">
    <li>January (6)</li><li>February (9)</li><li>March (4)</li><li>April (4)</li><li>June (5)</li><li>July (7)</li><li>August (8)</li>
  </ul>
  <h3 class="abs f-head" style="left:415px">Tags</h3>
  <p class="abs tags">News, dolor sit amet, consectetur, BLOGS, adipisicing elit, sed do eiusmod, tempor, Donation, ut labore et</p>
  <h3 class="abs f-head" style="left:549px">Newsletter</h3>
  <div class="abs email">Enter your Email</div>
  <div class="abs submit">Submit</div>
  <div class="abs bottom">Copyright@rancholasbrumas.2014.All Rights Reserved.</div>
</footer>
</body>
</html>
```